Flyer-Design für Pflegeberatung
Zielgruppe
Ich würde gerne einen Flyer zur Pflegeberatung erstellen lassen. Zielgruppe sollen Senioren und Ihre Angehörigen sein.
Vielen Patienten benötigen eine Höherstufung des Pflegegrades oder bekommen keine Leistungen ausgezahlt ausgezahlt wenn Sie einen Pflegedienst beanspruchen. Hier benötigen wir einen originellen Flyer .
Aufgabenstellung
Ein kreativer und mutiger Flyer soll erstellt werden,
Es geht darum , dass wir die Leute beraten ,wie Sie mehr Pflegegeld bekommen.
Vielleicht können wir ein günstigeres Angebot unterbreiten, als der bisherige Pflegedienst.
Folgenden Text würde ich gerne einfügen:
Überschrift: Mehr Pflegegeld für Ihre Versorgung zu Hause
Reicht das Pflegegelt für Ihre Persönliche Versorgung nicht mehr aus?
Bleibt von Ihrem Pflegebudget kaum etwas für übrig?
Gerne beraten wir Sie zur Optimierung Ihrer Leistungen und planen gemeinsam, wie Sie trotz einer sehr guten Versorgung mehr Pflegegelt für sich behalten können.
Rufen Sie uns an,, wir beraten Sie sehr gerne telefonisch oder vereinbaren einen Beratungstermin bei Ihnen zu Hause.
Der Flyer wäre für zwei Pflegedienste zu erstellen.
Der Text und Grafik bleiben gleich, anzupassen wäre nur das Logo und die Adresse:
1. Adresse: Betreuungshaus Lindental GmbH, Kastanienweg 7 in 18432 Rostock, Tel 0381- 52146087
1. Adresse: hauskrankenpflege Velaris GmbH Birkenhainer Strasse 41 in Gnoien Tel 039971-541726

```html
<!DOCTYPE html>
<html lang="de">
<head>
<meta charset="UTF-8">
<title>Flyer Pflegeberatung – Betreuungshaus Lindental</title>
<link href="https://fonts.googleapis.com/css2?family=Poppins:ital,wght@0,600;0,700;0,800;1,600;1,700;1,800&display=swap" rel="stylesheet">
<style>
  :root {
    --backdrop: #d4d4d4;
    --paper: #f4f4f4;
    --brand-blue: #3d93d1;
    --ink-navy: #2e3656;
    --accent-pink: #d462ad;
    --accent-pink-deep: #cc5ba6;
    --lavender: #b79bd6;
    --white: #ffffff;
  }
  html, body {
    margin: 0;
    width: 1200px;
    height: 900px;
    overflow: hidden;
    background: var(--backdrop);
    font-family: "Poppins", sans-serif;
  }
  .flyer {
    position: absolute;
    width: 551px;
    height: 367px;
    overflow: hidden;
    box-shadow: 2px 3px 4px rgba(0,0,0,0.18);
  }
  /* Front side */
  .flyer--info {
    left: 187px;
    top: 74px;
    background: var(--paper);
  }
  .brand {
    position: absolute;
    left: 45px;
    top: 9px;
    display: flex;
    align-items: center;
    gap: 14px;
  }
  .brand__dot {
    width: 60px;
    height: 60px;
    border-radius: 50%;
    border: 4px solid var(--brand-blue);
    box-sizing: border-box;
  }
  .brand__name {
    font-weight: 700;
    font-size: 25px;
    color: var(--ink-navy);
    letter-spacing: -0.2px;
  }
  .question {
    position: absolute;
    left: 52px;
    margin: 0;
    font-weight: 700;
    font-style: italic;
    font-size: 16px;
    line-height: 19px;
    color: var(--brand-blue);
  }
  .question--first { top: 88px; }
  .question--second { top: 146px; }
  .copy {
    position: absolute;
    left: 48px;
    width: 460px;
    margin: 0;
    font-weight: 600;
    font-style: italic;
    font-size: 12px;
    line-height: 19px;
    color: var(--ink-navy);
  }
  .copy--advice { top: 191px; }
  .copy--call { top: 268px; }
  .footer-wave {
    position: absolute;
    left: 0;
    bottom: 0;
    width: 551px;
    height: 62px;
  }
  .contact-line {
    position: absolute;
    left: 48px;
    top: 338px;
    margin: 0;
    font-weight: 700;
    font-style: italic;
    font-size: 15px;
    color: var(--white);
    white-space: nowrap;
    word-spacing: 1px;
  }
  .contact-line .sep { margin: 0 6px; font-style: normal; }

  /* Back side */
  .flyer--cover {
    left: 462px;
    top: 463px;
    background: var(--accent-pink-deep);
  }
  .cover-photo {
    position: absolute;
    left: 0;
    top: 0;
    width: 345px;
    height: 367px;
  }
  .headline {
    position: absolute;
    margin: 0;
    color: var(--white);
    font-style: italic;
    white-space: nowrap;
  }
  .headline--big {
    left: 224px;
    top: 148px;
    font-size: 60px;
    font-weight: 800;
    font-style: normal;
    letter-spacing: -1px;
    line-height: 1;
  }
  .headline--keyword {
    right: 34px;
    top: 200px;
    font-size: 28px;
    font-weight: 700;
    line-height: 1;
  }
  .headline--line {
    left: 224px;
    font-size: 28px;
    font-weight: 700;
    line-height: 1;
  }
  .headline--care { top: 236px; }
  .headline--home { top: 271px; }
  .cover-arrow {
    position: absolute;
    left: 375px;
    top: 310px;
    width: 160px;
    height: 40px;
  }
</style>
</head>
<body>

<section class="flyer flyer--info">
  <div class="brand">
    <span class="brand__dot"></span>
    <span class="brand__name">Betreuungshaus Lindental</span>
  </div>

  <h2 class="question question--first">Reicht das Pflegegelt für Ihre<br>Persönliche Versorgung nicht mehr aus?</h2>
  <h2 class="question question--second">Bleibt von Ihrem Budget kaum etwas für übrig?</h2>

  <p class="copy copy--advice">Gerne beraten wir Sie zur Optimierung Ihrer Leistungen und planen gemeinsam, wie Sie trotz einer sehr guten Versorgung mehr Pflege-gelt für sich behalten können.</p>
  <p class="copy copy--call">Rufen Sie uns an,, wir beraten Sie sehr gerne telefonisch oder vereinbaren einen Beratungstermin bei Ihnen zu Hause.”</p>

  <svg class="footer-wave" viewBox="0 0 551 62" preserveAspectRatio="none" aria-hidden="true">
    <path d="M0 16 C 60 10, 110 24, 200 22 C 300 20, 380 0, 470 1 C 510 2, 535 6, 551 10 L 551 62 L 0 62 Z" fill="var(--accent-pink)"/>
  </svg>
  <p class="contact-line">Kastanienweg 7<span class="sep">•</span>18432 Rostock<span class="sep">&nbsp;•</span>Tel 0381- 52146087</p>
</section>

<section class="flyer flyer--cover">
  <svg class="cover-photo" viewBox="0 0 345 367" role="img" aria-label="Foto: fröhliche Seniorin mit pinker Sonnenbrille, lila Fellmantel und Goldketten, Geldscheine in der Manteltasche">
    <defs>
      <linearGradient id="photoTone" x1="0" y1="0" x2="1" y2="1">
        <stop offset="0" stop-color="var(--accent-pink-deep)"/>
        <stop offset="0.45" stop-color="var(--lavender)"/>
        <stop offset="1" stop-color="#5a4a66"/>
      </linearGradient>
    </defs>
    <path d="M0 60 C 40 20, 120 0, 200 10 C 280 20, 300 120, 290 200 C 300 260, 320 320, 340 367 L 0 367 Z" fill="url(#photoTone)"/>
  </svg>

  <h1 class="headline headline--big">Mehr</h1>
  <p class="headline headline--keyword">Pflegegeld</p>
  <p class="headline headline--line headline--care">für Ihre Versorgung</p>
  <p class="headline headline--line headline--home">zu Hause!</p>

  <svg class="cover-arrow" viewBox="0 0 160 40" aria-hidden="true">
    <path d="M6 6 C 40 28, 100 36, 150 28" fill="none" stroke="var(--white)" stroke-width="2" stroke-linecap="round"/>
    <path d="M134 20 L 152 28 L 136 38" fill="none" stroke="var(--white)" stroke-width="2" stroke-linecap="round" stroke-linejoin="round"/>
  </svg>
</section>

</body>
</html>
```